Website design for an events management company

What we need is the design of a website to be used by an events management company, the company is called "Velto Conference Services" and the website is expected to contain the following sections:
1) Homepage
2) Who are we?
3) Mission / Vision / Core values
4) Why to choose Velto?
5) Past experience
6) Duties or provided services (Scientific Program Duties, Accreditation, Fund Raising, Accommodations, Social Activities, Transportation, Marketing of the Event, Publications and printed materials, Secretarial Work and Media Coverage)
7) References
8) Contact Us page (will probably contain a contact us form plus email, address and a google map)

Attached for your reference the company's logo

Expected that the winner should deliver the designs of at least two pages (the homepage plus an inner page) plus of course all the used graphics, images ... etc.

Thanks

Target Market(s)

The design need to target scientific events and not public events, for example the company doesn't organize music concerts ... etc., it organizes only scientific events so please target business users (i.e. doctors, engineers, scientisits ... etc) while making the designs, including the correct colors, images and icons

Industry/Entity Type

It Company

Number of Pages Required

2 page

Requirements
Must have
• One homepage
• One inner page
• All the used graphics and images
Nice to have
• More than two pages

```html
<!DOCTYPE html>
<html lang="en">
<head>
<meta charset="utf-8">
<title>Velto Conference Services</title>
<link href="https://fonts.googleapis.com/css2?family=Arimo:wght@400;700&family=Open+Sans:ital,wght@0,400;0,600;1,400&display=swap" rel="stylesheet">
<style>
:root{
  --ink:#333;
  --muted:#666;
  --nav:#6d6e71;
  --nav-active:#8dc63f;
  --green:#8dc63f;
  --blue:#0a93d4;
  --purple:#8e3796;
  --orange:#f3901d;
  --lime:#7cb342;
  --red:#e52521;
  --yellow:#f0c419;
  --cyan:#1a9ad6;
  --violet:#5c2d91;
  --panel:#ebebeb;
  --hero:#9cc6e8;
  --map:#8a8b8e;
  --white:#fff;
}
*{box-sizing:border-box;margin:0;padding:0}
html,body{width:686px;height:1200px;overflow:hidden;background:var(--white)}
body{position:relative;font-family:"Open Sans",Arial,sans-serif;color:var(--ink)}
.abs{position:absolute}
.rainbow{position:absolute;left:0;width:686px;height:2px;background:linear-gradient(90deg,#e52521,#f3901d,#f0c419,#8dc63f,#1a9ad6,#5c2d91,#8e3796)}
.brand{left:57px;top:14px;display:flex;align-items:center;gap:6px}
.brand-dot{width:14px;height:14px;border-radius:50%;background:var(--purple)}
.brand-name{font-family:"Arimo",Arial,sans-serif;font-weight:700;font-size:14px;color:var(--nav);line-height:1}
.brand-sub{left:57px;top:34px;font-family:"Arimo",Arial,sans-serif;font-size:6px;color:var(--muted)}
.contact-item{top:19px;display:flex;align-items:center;gap:6px;font-family:"Arimo",Arial,sans-serif;font-weight:700;font-size:8.5px}
.contact-item .ring{width:26px;height:26px;border-radius:50%;border:2px solid;display:flex;align-items:center;justify-content:center}
.phone{left:332px;color:var(--blue)}
.phone .ring{border-color:var(--purple)}
.mail{left:458px;color:var(--orange)}
.mail .ring{border-color:var(--green)}
.contact-sep{left:449px;top:18px;width:1px;height:28px;background:#ddd}
.nav{left:0;top:62px;width:686px;height:25px;background:var(--nav);display:flex;align-items:center;padding-left:55px;gap:20px}
.nav a{font-family:"Arimo",Arial,sans-serif;font-weight:700;font-size:7.4px;color:var(--white);text-decoration:none;text-transform:uppercase}
.nav a.active{color:var(--nav-active)}
.hero{left:0;top:87px;width:686px;height:205px;background:var(--hero)}
.hero-title{left:0;top:233px;width:686px;text-align:center;font-family:"Arimo",Arial,sans-serif;font-weight:700;font-size:23px;color:#111;letter-spacing:.2px}
.dots{left:323px;top:276px;display:flex;gap:2px}
.dots i{width:8px;height:8px;border-radius:50%;border:1.2px solid var(--white);display:block}
.dots i.on{background:var(--blue)}
.mission{left:0;top:292px;width:686px;height:44px;background:var(--blue)}
.mission-tag{left:0;top:292px;width:160px;height:44px;background:var(--green);clip-path:polygon(0 0,148px 0,160px 22px,148px 44px,0 44px)}
.mission-label{left:57px;top:301px;font-family:"Arimo",Arial,sans-serif;font-weight:700;font-size:10.5px;color:var(--white);line-height:13px}
.mission-text{left:179px;top:300px;width:430px;font-style:italic;font-size:7.4px;line-height:13px;color:var(--white)}
.section-title{left:0;width:686px;text-align:center;font-family:"Arimo",Arial,sans-serif;font-weight:700;font-size:12.5px;color:var(--ink)}
.divider{left:308px;width:70px;height:8px}
.divider::before{content:"";position:absolute;left:0;right:0;top:3.5px;height:1px;background:#ccc}
.divider::after{content:"";position:absolute;left:31px;top:0;width:8px;height:8px;border-radius:50%;background:var(--white);border:1.5px solid var(--purple)}
.intro{left:143px;top:389px;width:400px;text-align:center;font-size:6.4px;line-height:13px;color:var(--muted)}
.svc{width:110px;text-align:center}
.svc .ring{margin:0 auto;width:62px;height:62px;border-radius:50%;border:3.5px solid;display:flex;align-items:center;justify-content:center;background:var(--white)}
.svc span{display:block;margin-top:11px;font-family:"Arimo",Arial,sans-serif;font-weight:700;font-size:6.8px;color:#444;text-transform:uppercase;white-space:nowrap}
.work{left:0;top:770px;width:686px;height:254px;background:var(--panel)}
.card{top:842px;width:176px}
.card .photo{width:176px;height:101px;border:2px solid var(--white);box-shadow:0 0 2px rgba(0,0,0,.2)}
.card h3{margin-top:14px;text-align:center;font-family:"Arimo",Arial,sans-serif;font-weight:700;font-size:8.8px;color:var(--ink)}
.card p{margin-top:6px;text-align:center;font-size:6.4px;line-height:13px;color:var(--muted)}
.footer{left:0;top:1026px;width:686px;height:174px;background:var(--nav)}
.foot-brand{left:57px;top:1062px;display:flex;align-items:center;gap:6px}
.foot-brand .brand-dot{background:var(--white)}
.foot-brand .brand-name{color:var(--white);font-size:15px}
.foot-h{top:1046px;font-family:"Arimo",Arial,sans-serif;font-weight:700;font-size:8.6px;color:var(--white)}
.links{top:1065px;font-size:6.6px;line-height:12.2px;color:var(--white)}
.field{left:288px;width:89px;height:15px;background:var(--white);font-size:6.3px;color:#999;padding:3px 5px}
.message{left:380px;top:1064px;width:101px;height:52px;background:var(--white);font-size:6.3px;color:#999;padding:4px 6px}
.send{left:443px;top:1119px;width:38px;height:20px;background:#7cc242;color:var(--white);font-family:"Arimo",Arial,sans-serif;font-weight:700;font-size:7px;display:flex;align-items:center;justify-content:center}
.map{left:502px;top:1068px;width:130px;height:67px;background:var(--map);border-radius:4px}
.foot-rule{left:0;top:1150px;width:686px;height:1px;background:#7d7e81}
.cal{left:57px;top:1156px;width:30px;height:34px;background:var(--white);border-top:7px solid var(--red);border-radius:2px}
.copy{left:94px;top:1165px;font-size:6.6px;color:var(--white)}
.social{top:1164px;width:16px;height:16px;border-radius:3px;background:#d7d7d8}
</style>
</head>
<body>
<div class="rainbow" style="top:0"></div>

<header>
  <div class="abs brand"><div class="brand-dot"></div><div class="brand-name">Velto</div></div>
  <div class="abs brand-sub">Velto Conference Services</div>

  <div class="abs contact-item phone">
    <div class="ring"><svg width="11" height="11" viewBox="0 0 24 24"><path fill="#8e3796" d="M6.6 10.8a15 15 0 0 0 6.6 6.6l2.2-2.2c.3-.3.7-.4 1-.2 1.1.4 2.3.6 3.6.6.6 0 1 .4 1 1V20c0 .6-.4 1-1 1A17 17 0 0 1 3 4c0-.6.4-1 1-1h3.5c.6 0 1 .4 1 1 0 1.3.2 2.5.6 3.6.1.3 0 .7-.2 1z"/></svg></div>
    020 - 4455 - 7788
  </div>
  <div class="abs contact-sep"></div>
  <div class="abs contact-item mail">
    <div class="ring"><svg width="11" height="9" viewBox="0 0 24 18"><rect width="24" height="18" rx="2" fill="#8dc63f"/><path d="M1 2l11 8 11-8" fill="none" stroke="#fff" stroke-width="2"/></svg></div>
    info@veltoconference.com
  </div>
</header>

<nav class="abs nav">
  <a class="active" href="#">Home</a><a href="#">Who are we</a><a href="#">Mission</a><a href="#">Vision</a><a href="#">Why to choose Velto?</a><a href="#">Past experience</a><a href="#">Services</a><a href="#">References</a><a href="#">Contact us</a>
</nav>

<section>
  <div class="abs hero" role="img" aria-label="Hero slide photo: outdoor landscape with a rainbow and a tree"></div>
  <div class="abs hero-title">BE POSITIVE ....... BE CREATIVE</div>
  <div class="abs dots"><i class="on"></i><i></i><i></i><i></i></div>
</section>

<section>
  <div class="abs mission"></div>
  <div class="abs mission-tag"></div>
  <div class="abs mission-label">OUR<br>MISSION</div>
  <p class="abs mission-text">To distinguish ourselves in the event management market by managing, producing and supporting outstanding events that exceed customers increasing expectations in terms of value, service and innovation.</p>
</section>

<section>
  <h2 class="abs section-title" style="top:355px">OUR SERVICES</h2>
  <div class="abs divider" style="top:375px"></div>
  <p class="abs intro">Velto works in managing events by creative and innovative approaches creating a long lasting satisfaction and ease of work between its clients. Our market existence, business model and operation strategies made us unique..</p>

  <div class="abs svc" style="left:75px;top:449px"><div class="ring" style="border-color:var(--purple)"><svg width="22" height="22" viewBox="0 0 24 24"><circle cx="12" cy="10" r="7" fill="none" stroke="#8e3796" stroke-width="2"/><path d="M8 16l-2 7 6-3 6 3-2-7" fill="#8e3796"/></svg></div><span>High reputation</span></div>
  <div class="abs svc" style="left:207px;top:449px"><div class="ring" style="border-color:var(--orange)"><svg width="22" height="22" viewBox="0 0 24 24"><circle cx="12" cy="12" r="6" fill="none" stroke="#f3901d" stroke-width="4" stroke-dasharray="3 2"/><circle cx="12" cy="12" r="2" fill="#f3901d"/></svg></div><span>Quality of services</span></div>
  <div class="abs svc" style="left:373px;top:449px"><div class="ring" style="border-color:var(--lime)"><svg width="22" height="22" viewBox="0 0 24 24"><circle cx="14" cy="10" r="6" fill="none" stroke="#7cb342" stroke-width="2"/><path d="M10 14l-6 6" stroke="#7cb342" stroke-width="3"/></svg></div><span>Transparency of work</span></div>
  <div class="abs svc" style="left:499px;top:449px"><div class="ring" style="border-color:var(--red)"><svg width="22" height="22" viewBox="0 0 24 24"><circle cx="12" cy="10" r="6" fill="#e52521"/><rect x="9" y="16" width="6" height="4" fill="#e52521"/></svg></div><span>Creativity</span></div>

  <div class="abs svc" style="left:36px;top:548px"><div class="ring" style="border-color:var(--orange)"><svg width="22" height="22" viewBox="0 0 24 24"><path d="M4 11h4v10H4zM9 11l4-8c2 0 2 2 2 3l-1 4h6c1 0 2 1 1.5 2l-2 8c-.3 1-1 1-2 1H9z" fill="#f3901d"/></svg></div><span>Guarantee</span></div>
  <div class="abs svc" style="left:159px;top:548px"><div class="ring" style="border-color:var(--violet)"><svg width="22" height="22" viewBox="0 0 24 24"><rect x="3" y="7" width="18" height="13" rx="2" fill="#5c2d91"/><path d="M9 7V4h6v3" fill="none" stroke="#5c2d91" stroke-width="2"/></svg></div><span>Professional</span></div>
  <div class="abs svc" style="left:421px;top:548px"><div class="ring" style="border-color:var(--yellow)"><svg width="22" height="22" viewBox="0 0 24 24"><path d="M3 3l7 7M21 3l-7 7M3 21l7-7M21 21l-7-7M3 3h5M3 3v5M21 3h-5M21 3v5M3 21h5M3 21v-5M21 21h-5M21 21v-5" stroke="#f0c419" stroke-width="2.4" fill="none"/></svg></div><span>Flexibility</span></div>
  <div class="abs svc" style="left:540px;top:548px"><div class="ring" style="border-color:var(--cyan)"><svg width="22" height="22" viewBox="0 0 24 24"><rect x="6" y="2" width="12" height="20" fill="#1a9ad6"/><path d="M9 6h2M13 6h2M9 10h2M13 10h2M9 14h2M13 14h2" stroke="#fff" stroke-width="2"/></svg></div><span>Establishment</span></div>

  <div class="abs svc" style="left:75px;top:648px"><div class="ring" style="border-color:var(--yellow)"><svg width="22" height="22" viewBox="0 0 24 24"><ellipse cx="12" cy="11" rx="9" ry="7" fill="none" stroke="#f0c419" stroke-width="2"/><path d="M7 17l-2 4 5-3" fill="#f0c419"/></svg></div><span>Customer satisfaction</span></div>
  <div class="abs svc" style="left:207px;top:648px"><div class="ring" style="border-color:var(--lime)"><svg width="22" height="22" viewBox="0 0 24 24"><path d="M3 9l4-5h10l4 5-9 12z" fill="none" stroke="#7cb342" stroke-width="2"/><path d="M3 9h18" stroke="#7cb342" stroke-width="2"/></svg></div><span>Perfection</span></div>
  <div class="abs svc" style="left:373px;top:648px"><div class="ring" style="border-color:var(--purple)"><svg width="22" height="22" viewBox="0 0 24 24"><path d="M4 12l6 6L20 6" fill="none" stroke="#8e3796" stroke-width="3.5"/></svg></div><span>Ease of work</span></div>
  <div class="abs svc" style="left:499px;top:648px"><div class="ring" style="border-color:var(--violet)"><svg width="24" height="22" viewBox="0 0 24 22"><circle cx="6" cy="7" r="3" fill="#8e3796"/><circle cx="18" cy="7" r="3" fill="#8e3796"/><circle cx="12" cy="6" r="4" fill="#8e3796"/><path d="M5 20v-5a7 7 0 0 1 14 0v5z" fill="#8e3796"/></svg></div><span>Managing outstanding events</span></div>
</section>

<div class="rainbow" style="top:767px"></div>
<section>
  <div class="abs work"></div>
  <h2 class="abs section-title" style="top:792px">OUR LATEST WORK</h2>
  <div class="abs divider" style="top:814px"></div>

  <article class="abs card" style="left:57px">
    <div class="photo" role="img" aria-label="Photo of a speaker at a laptop facing a conference audience" style="background:linear-gradient(135deg,#1e3a6e 0%,#b5532a 55%,#e69a3b 100%)"></div>
    <h3>Thrombosis &amp; Hemostasis</h3>
    <p>The 16th Annual conference of the working Group<br>of Thrombosis &amp; Hemostatsis</p>
  </article>
  <article class="abs card" style="left:255px">
    <div class="photo" role="img" aria-label="Photo of a seated audience applauding at a medical conference" style="background:linear-gradient(135deg,#5a3a2a 0%,#c9a68a 50%,#f0e4d4 100%)"></div>
    <h3>National Cardiac Society</h3>
    <p>The 17th Annual Heart Failure Conference of the<br>National Cardiac Society</p>
  </article>
  <article class="abs card" style="left:452px">
    <div class="photo" role="img" aria-label="Photo of a presenter in a bright seminar room with attendees" style="background:linear-gradient(135deg,#e7edf0 0%,#b9c6cc 50%,#4e5a66 100%)"></div>
    <h3>Conference</h3>
    <p>The 1st Annual Police International Cardiology<br>Confernce</p>
  </article>
</section>

<div class="rainbow" style="top:1024px"></div>
<footer>
  <div class="abs footer"></div>
  <div class="abs foot-brand"><div class="brand-dot"></div><div class="brand-name">Velto</div></div>

  <h4 class="abs foot-h" style="left:141px">INFORMATION</h4>
  <div class="abs links" style="left:141px">Home<br>Who are we<br>Mission<br>Vision<br>Why to choose Velto</div>
  <div class="abs links" style="left:214px">Past experience<br>Services<br>References<br>Contact us</div>

  <h4 class="abs foot-h" style="left:288px">CONTACT US</h4>
  <div class="abs field" style="top:1064px">Name :</div>
  <div class="abs field" style="top:1085px">Email :</div>
  <div class="abs field" style="top:1103px">Title :<svg style="position:absolute;right:6px;top:6px" width="6" height="4" viewBox="0 0 6 4"><path d="M0 0h6L3 4z" fill="#999"/></svg></div>
  <div class="abs message">Message :</div>
  <div class="abs send">SEND</div>

  <h4 class="abs foot-h" style="left:501px">LOCATION</h4>
  <div class="abs map" role="img" aria-label="World map showing office location"></div>

  <div class="abs foot-rule"></div>
  <div class="abs cal" role="img" aria-label="Calendar illustration"></div>
  <div class="abs copy">© 2016, Velto Conference Services. All Rights Reserved.</div>
  <div class="abs social" style="left:539px"></div>
  <div class="abs social" style="left:563px"></div>
  <div class="abs social" style="left:587px"></div>
  <div class="abs social" style="left:613px"></div>
</footer>
</body>
</html>
```